Banner for a National Dental Conference

We need a banner logo for our next Dental Conference in 2017. Our theme is 'Challenging the Status Quo'.
It must have the words '20 years of oral health therapy in Victoria' and the conference date and venue:
7-8th April 2017
Wattlebrook Shore Lodge, Torquay, Victoria.
It must also feature our association logo as attached.
Please be creative, however, we would like a 'clean' design, not cluttered.
The design is intended for use in the conference program and website.

Target Market(s)

Dental practitioners

Industry/Entity Type

Dental

Requirements
Must have
• As above.

```html
<!DOCTYPE html>
<html lang="en">
<head>
<meta charset="utf-8">
<title>Oral Health Therapy Conference Banner</title>
<link rel="stylesheet" href="https://fonts.googleapis.com/css2?family=Archivo+Black&family=Oswald:wght@400;500&family=Crimson+Text:wght@700&display=swap">
<style>
  :root {
    --page: #ffffff;
    --banner-light: #f7f7f8;
    --banner-mid: #e4e4e6;
    --purple: #5a3592;
    --green: #12805a;
    --green-light: #27b07a;
    --ink: #3a3a3c;
    --photo-skin: #e9c3a8;
    --photo-light: #f5e6dc;
    --white: #ffffff;
  }
  * { margin: 0; padding: 0; box-sizing: border-box; }
  html, body {
    width: 1200px;
    height: 1200px;
    overflow: hidden;
    background: var(--page);
  }
  .canvas {
    position: relative;
    width: 1200px;
    height: 1200px;
  }
  .banner {
    position: absolute;
    left: 34px;
    top: 476px;
    width: 1132px;
    height: 182px;
    overflow: hidden;
    background: linear-gradient(90deg, var(--banner-mid) 0%, var(--banner-light) 25%, var(--white) 50%, var(--banner-light) 75%, var(--banner-mid) 100%);
  }
  .banner-art {
    position: absolute;
    inset: 0;
  }
  .brand {
    position: absolute;
    left: 30px;
    top: 30px;
    display: flex;
    align-items: center;
    gap: 12px;
    font-family: "Oswald", sans-serif;
    font-weight: 400;
    font-size: 54px;
    line-height: 1;
    letter-spacing: 4px;
    color: var(--purple);
  }
  .brand-dot {
    width: 16px;
    height: 16px;
    border-radius: 50%;
    background: var(--green);
  }
  .event-info {
    position: absolute;
    left: 762px;
    top: 0;
    width: 340px;
    height: 182px;
  }
  .event-line {
    position: absolute;
    left: 0;
    width: 100%;
    text-align: center;
    white-space: nowrap;
  }
  .event-title {
    top: 6px;
    font-family: "Archivo Black", sans-serif;
    font-size: 42px;
    line-height: 44px;
    letter-spacing: 1px;
    color: var(--green);
    background: linear-gradient(180deg, var(--green-light) 0%, var(--green) 70%);
    -webkit-background-clip: text;
    background-clip: text;
    -webkit-text-fill-color: transparent;
  }
  .event-subtitle {
    top: 50px;
    font-family: "Oswald", sans-serif;
    font-weight: 500;
    font-size: 21.5px;
    line-height: 24px;
    letter-spacing: 0.6px;
    color: var(--ink);
  }
  .event-date {
    top: 84px;
    font-family: "Archivo Black", sans-serif;
    font-size: 33px;
    line-height: 38px;
    color: var(--green);
    background: linear-gradient(180deg, var(--green-light) 0%, var(--green) 70%);
    -webkit-background-clip: text;
    background-clip: text;
    -webkit-text-fill-color: transparent;
  }
  .event-venue-row {
    top: 132px;
  }
  .event-venue {
    display: inline-block;
    height: 27px;
    padding: 3px 12px;
    border-radius: 14px;
    background: var(--purple);
    font-family: "Crimson Text", serif;
    font-weight: 700;
    font-size: 16.5px;
    line-height: 21px;
    color: var(--white);
  }
</style>
</head>
<body>
<div class="canvas">
  <section class="banner">
    <svg class="banner-art" width="1132" height="182" viewBox="0 0 1132 182">
      <defs>
        <linearGradient id="photo-tone" x1="0" y1="0" x2="1" y2="0">
          <stop offset="0" stop-color="var(--photo-light)"/>
          <stop offset="0.5" stop-color="var(--photo-skin)"/>
          <stop offset="1" stop-color="var(--photo-light)"/>
        </linearGradient>
      </defs>
      <rect class="photo-area" role="img" aria-label="Photo of a smiling woman pointing at her white teeth" x="436" y="10" width="268" height="172" rx="4" fill="url(#photo-tone)"/>
      <path class="swoosh-purple" d="M0 148 C 80 196, 200 190, 330 120 C 450 55, 550 5, 640 8 L 644 13 C 555 12, 460 62, 338 128 C 210 196, 80 200, 0 156 Z" fill="var(--purple)"/>
      <path class="swoosh-green" d="M647 0 C 640 60, 690 110, 728 150 C 740 162, 738 175, 736 182 L 758 182 C 758 165, 752 150, 740 138 C 700 100, 655 60, 660 0 Z" fill="var(--green)"/>
    </svg>

    <div class="brand">
      <span>ORTAV</span>
      <span class="brand-dot"></span>
    </div>

    <div class="event-info">
      <h1 class="event-line event-title">20 YEARS OF</h1>
      <p class="event-line event-subtitle">ORAL HEALTH THERAPY IN VICTORIA</p>
      <p class="event-line event-date">7-8th April 2017</p>
      <p class="event-line event-venue-row"><span class="event-venue">Wattlebrook Shore Lodge, Torquay, Victoria.</span></p>
    </div>
  </section>
</div>
</body>
</html>
```